whitening gel shopping website design

Hello:
We would like to create a whitening gel selling website. It will be very close to Glowbrite, but different designs. https://us.glowbriteorals.example/

What is your organization or website name?
Velvet Beaming

Industry: health and beauty
Target user: ladies between 16 to 40, please make the website friendly and lovely

website pages: main website, shop products, enrolled monthly plans, about us, contact us, policy, customer login log out, shopping cart, customer dashboard.

Website main page contains:
1. one slide show that shows advertisements.
2. show current promo codes
3.show a brief overview about our history
4. show a brief overview about the product introduction
5. show a brief overview of our monthly enrolled product plan
6. have an area to show blogs and posts (please take a look at Glowbrite home page)
7. buttons for customer to login, sign up, visit home, about us, policy, returns, subscription etc.

Note: for the contest, please finish the website main page and the product page only, now we don’t have any logo, test or images, please use yours for now.

```html
<!DOCTYPE html>
<html lang="en">
<head>
<meta charset="utf-8">
<title>Velvet Beaming – Whitening Gel</title>
<link rel="stylesheet" href="https://fonts.googleapis.com/css2?family=Dancing+Script:wght@500;700&family=Lato:wght@400;700&display=swap">
<style>
:root{
  --pink:#ef1762;
  --pink-soft:#fbd6de;
  --pink-band:#eaa3d8;
  --violet:#9d86f2;
  --ink:#333;
  --muted:#777;
  --grey-bg:#f1f1f1;
  --white:#fff;
}
*{margin:0;padding:0;box-sizing:border-box}
html,body{width:1200px;height:3264px;overflow:hidden}
body{position:relative;background:var(--white);font-family:'Lato',sans-serif;color:var(--ink);font-size:11px;line-height:1.6}
.abs{position:absolute}
.script{font-family:'Dancing Script',cursive;color:var(--pink);font-weight:500}
.btn{display:inline-block;background:var(--pink);color:var(--white);font-size:9px;font-weight:700;letter-spacing:.5px;padding:7px 20px;text-transform:uppercase}
.btn-violet{background:var(--violet)}
.ph{display:block}

/* header */
.site-header{left:0;top:0;width:1200px;height:48px;background:var(--white);border-bottom:1px solid #eee}
.brand{left:150px;top:8px;font-size:24px;white-space:nowrap}
.main-nav{left:430px;top:16px;display:flex;gap:8px;font-size:10px}
.main-nav a,.account-nav a{color:var(--ink);text-decoration:none;padding:2px 10px}
.main-nav a.active{background:var(--pink);color:var(--white);border-radius:3px}
.account-nav{left:930px;top:16px;display:flex;gap:6px;font-size:10px}

/* hero */
.hero{left:0;top:48px;width:1200px;height:342px;background:linear-gradient(100deg,#fde7ec 0%,#fbd2dc 55%,#f9c4d1 100%)}
.hero-title{left:215px;top:165px;font-size:34px;color:#2b2b2b;font-family:'Dancing Script',cursive;font-weight:700;white-space:nowrap}
.hero-btn{left:290px;top:222px}
.hero-art{left:720px;top:70px;width:230px;height:230px;background:linear-gradient(160deg,#f7c3d0,#f3aabf)}
.arrow{width:32px;height:32px;border-radius:50%;background:var(--pink);color:var(--white);display:flex;align-items:center;justify-content:center}
.hero-prev{left:28px;top:155px}
.hero-next{left:1120px;top:155px}
.dots{left:556px;top:372px;display:flex;gap:6px}
.dots span{width:12px;height:12px;border-radius:50%;border:1px solid var(--pink);background:var(--white)}
.dots span.on{background:var(--pink)}

/* grey zone */
.grey-zone{left:0;top:390px;width:1200px;height:1200px;background:var(--grey-bg)}
.promo{left:0;top:510px;width:1200px;text-align:center}
.promo h2{font-size:20px;font-weight:400;letter-spacing:1px;color:#222}
.promo p{font-size:10px;color:var(--muted);margin:4px 0 8px}

.card{background:var(--white);box-shadow:0 2px 10px rgba(0,0,0,.08)}
.history{left:150px;top:640px;width:900px;height:360px}
.history-photo-a{left:15px;top:28px;width:140px;height:170px;background:linear-gradient(135deg,#8d6b56,#c9a38c)}
.history-photo-b{left:55px;top:145px;width:150px;height:120px;background:linear-gradient(135deg,#d9d4cf,#f3efea);border:3px solid var(--white)}
.history-body{left:245px;top:24px;width:620px}
.history-body h3{text-align:center;font-size:20px;margin-bottom:8px}
.history-body p{font-size:9.5px;color:var(--muted);margin-bottom:12px}
.history-body .more{font-size:9px;color:#aaa}

.products{left:150px;top:1048px;width:900px;height:472px}
.products h3{position:absolute;left:0;top:40px;width:900px;text-align:center;font-size:20px}
.products .sub{position:absolute;left:0;top:70px;width:900px;text-align:center;font-size:9px;color:var(--muted)}
.p-prev{left:18px;top:240px;background:var(--violet);width:26px;height:26px}
.p-next{left:856px;top:240px;background:var(--violet);width:26px;height:26px}
.product{top:138px;width:210px;height:295px;border:1px solid #eee;background:var(--white);text-align:center}
.product .pack{margin:22px auto 0;width:80px;height:120px;background:linear-gradient(180deg,#fff 0%,#3c7fd8 40%,#e23f55 100%);border:1px solid #dde}
.product p{font-size:9px;color:var(--muted);padding:30px 22px 0;height:84px;text-align:left;line-height:1.5}

/* plan band */
.plan{left:0;top:1590px;width:1200px;height:530px;background:linear-gradient(120deg,#f0b3df 0%,#e7a1d6 45%,#f5c8e8 100%)}
.plan h3{left:215px;top:35px;font-size:20px;white-space:nowrap}
.plan .sub{left:215px;top:72px;font-size:9px;color:#555}
.plan ul{left:215px;top:110px;width:360px;list-style:none;font-size:10px;color:#333}
.plan li{margin-bottom:14px}
.plan .btn{left:215px;top:255px}
.plan-photo{left:670px;top:60px;width:380px;height:410px;background:var(--white);padding:22px}
.plan-photo div{width:100%;height:100%;background:linear-gradient(150deg,#c8e3f4,#f4f6fb 45%,#e3a3b5)}

/* blog */
.blog-title{left:0;top:2180px;width:1200px;text-align:center;font-size:20px}
.post-img-a{left:0;top:2225px;width:600px;height:375px;background:linear-gradient(135deg,#cfcfcf,#8e7a6a 55%,#3fae6c)}
.post-img-b{left:600px;top:2600px;width:600px;height:390px;background:linear-gradient(180deg,#a8c6a0,#6f8b4f 55%,#a77b52)}
.post{width:600px;height:375px;background:var(--white);padding:40px 45px}
.post-head{display:flex;justify-content:space-between;align-items:baseline;margin-bottom:18px}
.post-head h4{font-size:14px;font-weight:400;letter-spacing:1px}
.post-head span{font-size:8px;color:var(--muted)}
.post p{font-size:9.5px;color:var(--muted);margin-bottom:22px}
.post-one{left:600px;top:2225px}
.post-two{left:0;top:2600px;height:390px}
.view-all{left:0;top:3012px;width:1200px;text-align:center;font-size:9px;color:var(--muted)}

/* footer */
.footer-line{left:0;top:3108px;width:1200px;height:2px;background:var(--pink)}
.social{left:504px;top:3155px;display:flex;gap:16px}
.social span{width:36px;height:36px;border-radius:50%;background:#111;display:block}
.copyright{left:0;top:3212px;width:1200px;text-align:center;font-size:8px;color:var(--muted)}
</style>
</head>
<body>

<header class="site-header abs">
  <div class="brand abs script">Velvet Beaming</div>
  <nav class="main-nav abs">
    <a class="active">Home</a><a>Shop</a><a>About Us</a><a>Subscription</a><a>Contact Us</a>
  </nav>
  <nav class="account-nav abs"><a>Login</a><a>Sign Up</a></nav>
</header>

<section class="hero abs">
  <div class="hero-title abs">Make Life more beautiful</div>
  <a class="btn hero-btn abs">Shop Now</a>
  <div class="hero-art abs ph" role="img" aria-label="Promotional illustration for the whitening gel"></div>
  <div class="arrow hero-prev abs"><svg width="10" height="12" viewBox="0 0 10 12"><path d="M7 1 2 6l5 5" fill="none" stroke="#fff" stroke-width="2"/></svg></div>
  <div class="arrow hero-next abs"><svg width="10" height="12" viewBox="0 0 10 12"><path d="M3 1l5 5-5 5" fill="none" stroke="#fff" stroke-width="2"/></svg></div>
</section>

<div class="grey-zone abs"></div>
<div class="dots abs"><span class="on"></span><span></span><span></span></div>

<section class="promo abs">
  <h2>GET 20% OFF</h2>
  <p>Get 20% off by using the following coupon code</p>
  <a class="btn">GLOW20</a>
</section>

<section class="history card abs">
  <div class="history-photo-a abs ph" role="img" aria-label="Photo of a smiling young woman"></div>
  <div class="history-photo-b abs ph" role="img" aria-label="Photo of a woman at a dental clinic"></div>
  <div class="history-body abs">
    <h3 class="script">Our History</h3>
    <p>Velvet Beaming began at a small kitchen table, where two friends mixed their first gentle whitening gel for sensitive teeth. They wanted a product that felt kind, looked lovely on a shelf and gave every girl a reason to smile brighter each morning without pain.</p>
    <p>Within a year the little recipe grew into a real studio. We worked with dentists, tested every formula with care and kept our promise of peroxide free gels that are safe, soft on enamel and easy to use at home.</p>
    <p>Today thousands of women trust Velvet Beaming for their daily glow. We still pack many orders by hand, answer each message ourselves and believe that a confident smile is the most beautiful thing you can wear anywhere.</p>
    <span class="more">more</span>
  </div>
</section>

<section class="products card abs">
  <h3 class="script">Our Products</h3>
  <div class="sub">Gentle gels for a brighter smile</div>
  <div class="arrow p-prev abs"><svg width="8" height="10" viewBox="0 0 10 12"><path d="M7 1 2 6l5 5" fill="none" stroke="#fff" stroke-width="2"/></svg></div>
  <div class="arrow p-next abs"><svg width="8" height="10" viewBox="0 0 10 12"><path d="M3 1l5 5-5 5" fill="none" stroke="#fff" stroke-width="2"/></svg></div>
  <article class="product abs" style="left:50px">
    <div class="pack ph" role="img" aria-label="Whitening gel box"></div>
    <p>Daily whitening gel with a soft mint taste, safe for sensitive teeth and easy to apply.</p>
    <a class="btn btn-violet">Shop</a>
  </article>
  <article class="product abs" style="left:345px">
    <div class="pack ph" role="img" aria-label="Whitening gel box"></div>
    <p>Night repair gel that brightens while you sleep and keeps enamel strong.</p>
    <a class="btn btn-violet">Shop</a>
  </article>
  <article class="product abs" style="left:640px">
    <div class="pack ph" role="img" aria-label="Whitening gel box"></div>
    <p>Travel pen with gentle gel for quick touch ups after coffee, tea or a glass of wine.</p>
    <a class="btn btn-violet">Shop</a>
  </article>
</section>

<section class="plan abs">
  <h3 class="script abs">Smile Grand Plan</h3>
  <div class="sub abs">Monthly gel refills delivered to your door</div>
  <ul class="abs">
    <li>• Choose your favourite gels once and receive a fresh refill box every month with free shipping.</li>
    <li>• Pause, skip or cancel any time from your dashboard and enjoy member prices on every order.</li>
  </ul>
  <a class="btn abs">Join Plan</a>
  <div class="plan-photo abs"><div class="ph" role="img" aria-label="Whitening kit with trays and gel syringes"></div></div>
</section>

<h3 class="blog-title script abs">Our Blog</h3>
<div class="post-img-a abs ph" role="img" aria-label="Photo of a smiling young man in a green shirt"></div>
<article class="post post-one abs">
  <div class="post-head"><h4>POST ONE</h4><span>12 January</span></div>
  <p>Five simple habits keep your smile bright between whitening sessions. Rinse with water after coffee, use a straw for cold drinks, brush gently twice a day and never skip floss. A soft brush and a calm routine protect enamel, while a weekly gel treatment keeps stains away so your teeth stay fresh, clean and glowing all month long.</p>
  <a class="btn">Read More</a>
</article>
<article class="post post-two abs">
  <div class="post-head"><h4>POST TWO</h4><span>26 January</span></div>
  <p>Planning a wedding, trip or big interview? Start your whitening routine two weeks before the day. Use the gel each evening, drink plenty of water and choose light meals that will not stain. Take a photo every few days to see your progress, relax and trust the process, because a confident smile always looks wonderful in every picture you share with friends.</p>
  <a class="btn">Read More</a>
</article>
<div class="post-img-b abs ph" role="img" aria-label="Photo of a woman walking on a sunny forest path"></div>
<div class="view-all abs">view all</div>

<div class="footer-line abs"></div>
<div class="social abs" aria-label="Social links"><span></span><span></span><span></span><span></span></div>
<div class="copyright abs">Copyright 2024 Velvet Beaming. All rights reserved.</div>

</body>
</html>
```